Creative Stationary For Security Solutions Company
Halvern Guard Services
Creative Stationary For Security Solutions Company - Security
Creative Brief
Professional
Wesley Kolvasky
wesley@halvernguard.example
www.halvernguard.example
California PI No. 51928 And California PPO No. 40261
Logo has been uploaded in different color variations. Feel free to experiment, however I prefer the logo with black highlights on the visor, nose and neck (#1 I believe) I will provide my phone numbers towards the end of the project. Thanks and have fun.
I would like to see my logo on one side and info on the other. But feel free to experiment.

```html
<!DOCTYPE html>
<html lang="en">
<head>
<meta charset="utf-8">
<title>Halvern Guard Services — Folder</title>
<link rel="stylesheet" href="https://fonts.googleapis.com/css2?family=Montserrat:wght@400;700&display=swap">
<style>
  :root {
    --backdrop: #e9e9e9;
    --paper: #ffffff;
    --ink: #111111;
    --orange: #f26f14;
    --fold: #9a9a9a;
    --ghost: #ececec;
    --muted: #444444;
  }
  * { box-sizing: border-box; margin: 0; padding: 0; }
  html, body { width: 1200px; height: 888px; overflow: hidden; }
  body {
    background: var(--backdrop);
    font-family: "Montserrat", Arial, sans-serif;
    position: relative;
  }
  .folder {
    position: absolute;
    left: 40px; top: 76px;
    width: 1120px; height: 735px;
    background: var(--paper);
    overflow: hidden;
    box-shadow: 0 4px 14px rgba(0,0,0,.18);
  }
  .folder__swoosh { position: absolute; inset: 0; width: 100%; height: 100%; }
  .folder__fold {
    position: absolute; left: 543px; top: 0; bottom: 0;
    border-left: 1px dashed var(--fold);
  }
  .ghost-mark {
    position: absolute; left: 60px; top: 90px;
    width: 360px;
    color: var(--ghost);
    font-weight: 700; font-size: 74px; line-height: 1;
    letter-spacing: 2px;
  }
  .ghost-mark__disc {
    width: 250px; height: 250px; border-radius: 50%;
    background: #f6f6f6; margin: 0 0 18px 40px;
  }
  .contact {
    position: absolute; left: 20px; top: 560px;
    list-style: none;
    font-size: 9.5px; color: var(--muted); line-height: 17px;
  }
  .contact li { display: flex; align-items: center; gap: 8px; }
  .contact svg { width: 10px; height: 10px; fill: var(--orange); flex: none; }
  .brand {
    position: absolute; left: 620px; top: 70px; width: 440px;
    text-align: center;
  }
  .brand__disc {
    width: 150px; height: 150px; border-radius: 50%;
    background: var(--orange); margin: 0 auto 26px;
  }
  .brand__name {
    font-weight: 700; font-size: 36px; line-height: 1.2;
    color: var(--ink); letter-spacing: 1px; text-transform: uppercase;
  }
</style>
</head>
<body>
  <main class="folder">
    <svg class="folder__swoosh" viewBox="0 0 1120 735" preserveAspectRatio="none" aria-hidden="true">
      <path d="M0,662 C420,640 800,560 1120,368 L1120,424 C800,598 400,652 0,676 Z" fill="var(--ink)"/>
      <path d="M0,682 C400,658 800,610 1120,432 L1120,735 L0,735 Z" fill="var(--orange)"/>
    </svg>
    <div class="folder__fold"></div>

    <section class="panel panel--back">
      <div class="ghost-mark" aria-hidden="true">
        <div class="ghost-mark__disc"></div>
      </div>
      <ul class="contact">
        <li><svg viewBox="0 0 10 10"><path d="M2 0h2l1 3-1.5 1a6 6 0 0 0 2.5 2.5L7 5l3 1v2a2 2 0 0 1-2 2A8 8 0 0 1 0 2a2 2 0 0 1 2-2z"/></svg>555-010-2841</li>
        <li><svg viewBox="0 0 10 10"><rect x="2" y="0" width="6" height="10" rx="1"/></svg>555-010-2847</li>
        <li><svg viewBox="0 0 10 10"><rect x="0" y="3" width="10" height="5" rx="1"/><rect x="2" y="0" width="6" height="3"/></svg>555-010-2850</li>
        <li><svg viewBox="0 0 10 10"><rect x="0" y="2" width="10" height="6"/></svg>wesley@halvernguard.example</li>
      </ul>
    </section>

    <section class="panel panel--front">
      <div class="brand">
        <div class="brand__disc" aria-hidden="true"></div>
        <p class="brand__name">Halvern Guard Services</p>
      </div>
    </section>
  </main>
</body>
</html>
```